New Business Card

Use website for color, logo and theme.

http://www.plumwickonline.com/

Back side of card should be programs listed on home page of website

1) Phone Number is (800) 555-0142 x23
2) Fax (240) 555-0187
3) Address is - 647 W Harlowe Street, Suite 312, Baltimore, MD 21201
4) NMLS #738516

```html
<!DOCTYPE html>
<html lang="en">
<head>
<meta charset="utf-8">
<title>Plumwick Financial – Business Card</title>
<link href="https://fonts.googleapis.com/css2?family=Josefin+Sans:wght@400;600;700&family=Roboto+Slab:wght@700;900&display=swap" rel="stylesheet">
<style>
  :root {
    --stage: #000000;
    --navy: #0d5a8a;
    --sky: #1a9de0;
    --ghost: #2f83b8;
    --ink: #000000;
    --banner-shadow: #0a4a73;
    --gold: #c8a94a;
    --lime: #a6cd3a;
    --white: #ffffff;
  }
  * { box-sizing: border-box; margin: 0; padding: 0; }
  html, body { width: 1200px; height: 530px; overflow: hidden; background: var(--stage); }
  .canvas { position: relative; width: 1200px; height: 530px; background: var(--stage); font-family: "Josefin Sans", sans-serif; }

  /* Front */
  .card-front { position: absolute; left: 14px; top: 41px; width: 580px; height: 331px; background: var(--sky); overflow: hidden; }
  .front-split { position: absolute; inset: 0; }
  .ghost-name { position: absolute; right: 22px; top: 62px; text-align: right; font-family: "Roboto Slab", serif; font-weight: 900; font-style: italic; font-size: 78px; line-height: 74px; color: var(--ghost); opacity: .75; letter-spacing: -1px; }
  .banner { position: absolute; left: 36px; top: 39px; width: 460px; height: 58px; }
  .banner svg { position: absolute; inset: 0; }
  .banner-name { position: absolute; left: 10px; top: 8px; font-family: "Roboto Slab", serif; font-weight: 700; font-size: 33px; color: var(--white); letter-spacing: .5px; white-space: nowrap; }
  .contact-list { position: absolute; left: 22px; top: 162px; list-style: none; }
  .contact-item { display: flex; align-items: flex-start; gap: 10px; height: 29px; font-size: 15px; font-weight: 600; color: var(--white); line-height: 18px; }
  .contact-item svg { flex: 0 0 auto; width: 20px; height: 20px; margin-top: -3px; }
  .contact-item .accent { color: var(--lime); }
  .contact-item.address { height: auto; }

  /* Back */
  .card-back { position: absolute; left: 602px; top: 184px; width: 577px; height: 329px; background: var(--lime); overflow: hidden; }
  .back-top { position: absolute; left: 0; top: 0; width: 100%; height: 170px; background: var(--navy); }
  .program-box { position: absolute; border-radius: 14px; text-align: center; display: flex; flex-direction: column; justify-content: center; font-size: 14px; line-height: 22px; color: var(--white); }
  .program-box h2 { font-size: 14.5px; font-weight: 700; color: var(--ink); line-height: 22px; }
  .program-traditional { left: 21px; top: 16px; width: 282px; height: 138px; border: 3px solid var(--gold); }
  .program-lowcredit { left: 323px; top: 26px; width: 249px; height: 127px; border: 3px solid var(--gold); }
  .program-lowcredit h2 { font-size: 15px; }
  .program-lowcredit p { font-size: 15px; line-height: 23px; }
  .program-alternative { left: 65px; top: 177px; width: 442px; height: 144px; border: 3px solid var(--sky); font-size: 16px; line-height: 26px; }
  .program-alternative h2 { font-size: 16px; line-height: 26px; }
</style>
</head>
<body>
<main class="canvas">

  <section class="card-front" aria-label="Business card front">
    <svg class="front-split" viewBox="0 0 580 331" width="580" height="331" aria-hidden="true">
      <polygon points="0,0 324,0 203,331 0,331" fill="var(--navy)"/>
    </svg>
    <div class="ghost-name" aria-hidden="true">PLUM<br>WICK<br>FINANCIAL</div>
    <div class="banner">
      <svg viewBox="0 0 460 58" width="460" height="58" aria-hidden="true">
        <polygon points="8,8 430,8 460,58 8,58" fill="var(--banner-shadow)"/>
        <polygon points="0,0 420,0 450,56 0,56" fill="var(--ink)"/>
      </svg>
      <h1 class="banner-name">PLUMWICK FINANCIAL</h1>
    </div>
    <ul class="contact-list">
      <li class="contact-item">
        <svg viewBox="0 0 20 20" aria-hidden="true"><rect width="20" height="20" rx="3" fill="var(--gold)"/><path d="M6 4c1 0 2 2 2 3s-1 1-1 2 2 3 3 3 1-1 2-1 3 1 3 2-1 3-3 3C8 16 4 12 4 7c0-2 1-3 2-3z" fill="var(--navy)"/></svg>
        <span><span class="accent">(800)</span> 555-0142 <span class="accent">x23</span></span>
      </li>
      <li class="contact-item">
        <svg viewBox="0 0 20 20" aria-hidden="true"><rect x="2" y="6" width="16" height="12" rx="2" fill="var(--gold)"/><rect x="5" y="1" width="10" height="7" fill="var(--gold)"/><rect x="6" y="3" width="8" height="1.4" fill="var(--navy)"/><rect x="5" y="10" width="3" height="2" fill="var(--navy)"/><rect x="9" y="10" width="3" height="2" fill="var(--navy)"/><rect x="5" y="13" width="3" height="2" fill="var(--navy)"/><rect x="9" y="13" width="3" height="2" fill="var(--navy)"/></svg>
        <span><span class="accent">(240)</span> 555-0187</span>
      </li>
      <li class="contact-item">
        <svg viewBox="0 0 20 20" aria-hidden="true"><rect x="2" y="3" width="16" height="14" fill="var(--gold)"/></svg>
        <span>#738516</span>
      </li>
      <li class="contact-item address">
        <svg viewBox="0 0 20 20" aria-hidden="true"><circle cx="10" cy="10" r="9" fill="none" stroke="var(--gold)" stroke-width="1.6"/><path d="M10 4.5l5 4.5h-1.5v5h-2.5v-3h-2v3h-2.5v-5h-1.5z" fill="var(--gold)"/></svg>
        <span>647 W Harlowe Street,<br>Suite 312, Baltimore, MD 21201</span>
      </li>
    </ul>
  </section>

  <section class="card-back" aria-label="Business card back">
    <div class="back-top"></div>
    <div class="program-box program-traditional">
      <h2>Traditional Loan Programs:</h2>
      <p>FHA loans starting at 580 score<br>FHA 203k starting at 600 score<br>VA starting at 600 score (100% LTV)<br>All Conventional loan programs</p>
    </div>
    <div class="program-box program-lowcredit">
      <h2>Low Credit Score Programs:</h2>
      <p>500 score up to 70% LTV<br>540 score up to 75% LTV<br>580 score up to 96.5% LTV</p>
    </div>
    <div class="program-box program-alternative">
      <h2>Alternative Loan Programs:</h2>
      <p>Investor Fix &amp; Flip Rehab Loans<br>Investor Stated Loans<br>Foreign National Loans<br>Limited Documentation Loans (1 year tax or W2)</p>
    </div>
  </section>

</main>
</body>
</html>
```